Plastic Surgeon Needs a business card desing

I need a plastic surgeon business card, Im young , innovative , not afraid of thinking out of the box, What I dont like is human figures or scalpes as designing the card, because I think they are old fashion, I think my name is my strongest card, so I try to find the desing to be something elegant , simple , slick , stylish , radiant with carimsa!

Target Market(s)

PLastics Surgery Patients and doctors to have my data

Industry/Entity Type

Plastic

Contact Information for Business Card

phone numbers need to be legible , right now i have grey scales so they a not to legible

Font styles to use
Serif
Sans Serif

Requirements
Must have
• Personality, and it has to look like a doctor card, not a buisness man card, that is why i think it should be clean , clear , and legible
Nice to have
• Stylilsh, not to heavy card, in means of colors and logos, i think it should give a sensation of health
• Im not sure to have the logo of the hospital i work
Should not have
• human figures
• Hands
• Surgeons

```html
<!DOCTYPE html>
<html lang="es">
<head>
<meta charset="utf-8">
<title>Dr. Mateo Liranzo – Tarjeta de presentación</title>
<link rel="stylesheet" href="https://fonts.googleapis.com/css2?family=Arimo:wght@400&display=swap">
<style>
  :root {
    --backdrop: #e9e6e1;
    --card: #ffffff;
    --ink-grey: #4a4a4a;
    --ink-blue: #2e2e8f;
    --mark-grey: #b9b9bd;
    --card-shadow: rgba(0,0,0,0.18);
  }
  * { box-sizing: border-box; margin: 0; padding: 0; }
  html, body {
    width: 1200px; height: 892px; overflow: hidden;
    background: var(--backdrop);
    font-family: "Arimo", Arial, sans-serif;
  }
  .stage { position: relative; width: 1200px; height: 892px; }
  .card {
    position: absolute;
    width: 560px; height: 320px;
    background: var(--card);
    box-shadow: 0 6px 18px var(--card-shadow);
  }
  .card--back  { left: 560px; top: 90px; }
  .card--front { left: 80px;  top: 470px; }

  .brand { position: absolute; display: flex; align-items: flex-start; gap: 14px; }
  .brand__mark {
    width: 44px; height: 44px; border-radius: 50%;
    background: var(--mark-grey); flex: none;
  }
  .brand__text { padding-top: 30px; }
  .brand__name {
    font-size: 26px; letter-spacing: 0.5px;
    color: var(--ink-grey); line-height: 1;
  }
  .brand__tagline {
    margin-top: 4px; font-size: 15.5px;
    color: var(--ink-blue); white-space: nowrap;
  }
  .card--back .brand  { left: 130px; top: 130px; }
  .card--front .brand { left: 26px;  top: 24px; }

  .contact {
    position: absolute; left: 300px; top: 178px;
    font-size: 15px; line-height: 20px; color: var(--ink-grey);
  }
  .contact address { font-style: normal; }
</style>
</head>
<body>
<main class="stage">
  <section class="card card--back" aria-label="Reverso de la tarjeta">
    <div class="brand">
      <span class="brand__mark" aria-hidden="true"></span>
      <div class="brand__text">
        <p class="brand__name">DR. MATEO LIRANZO</p>
        <p class="brand__tagline">Cirugia plastica, estetica y reconstructiva</p>
      </div>
    </div>
  </section>

  <section class="card card--front" aria-label="Frente de la tarjeta">
    <div class="brand">
      <span class="brand__mark" aria-hidden="true"></span>
      <div class="brand__text">
        <p class="brand__name">DR. MATEO LIRANZO</p>
        <p class="brand__tagline">Cirugia plastica, estetica y reconstructiva</p>
      </div>
    </div>
    <div class="contact">
      <address>
        Calle Olmos 2185, Int. 304<br>
        Torre Medica Las Palmas<br>
        Monterrey, Nuevo Leon, Mexico
      </address>
      <p>P : 01 (55) 4821 7390</p>
      <p>C : 55 6102 4478</p>
      <p>E : mateo@drliranzo.com</p>
    </div>
  </section>
</main>
</body>
</html>
```